I need a box design created for a DNA Fitness Test

I need a modern and sleek box design for a fitness test. The box needs to have our logo on it and should be clean and modern. The Box is 9 Inches Long 3 and 3/4 inches wide, and 2 inches tall. Company logo attached. The company name is cedar vitality.

Target Market(s)

Fitness

Industry/Entity Type

Fitness

Requirements
Must have
• Our logo

```html
<!DOCTYPE html>
<html lang="en">
<head>
<meta charset="utf-8">
<title>Cedar Vitality – DNA Fitness Test Box Wrap</title>
<link rel="stylesheet" href="https://fonts.googleapis.com/css2?family=Montserrat:wght@800&display=swap">
<style>
  :root {
    --page-bg: #e2e5e8;
    --panel-white: #ffffff;
    --fold-line: #c4c7ca;
    --ink: #121212;
    --accent-blue: #1e8fe0;
    --tone-warm: #f6c9c4;
    --tone-warm-light: #fbe7d6;
    --tone-cool: #d9cdf0;
    --tone-cool-light: #d6e8f7;
    --tone-pink: #f4cde2;
  }
  html, body {
    margin: 0;
    padding: 0;
    width: 1200px;
    height: 1200px;
    overflow: hidden;
    background: var(--page-bg);
  }
  .wrap-sheet {
    position: absolute;
    left: 38px;
    top: 114px;
    width: 1124px;
    height: 972px;
    background: var(--panel-white);
  }
  .dieline {
    position: absolute;
    left: 12px;
    top: 12px;
    width: 1100px;
    height: 947px;
    border: 1px solid var(--fold-line);
    box-sizing: border-box;
  }
  .panel {
    position: absolute;
    left: 0;
    width: 100%;
    overflow: hidden;
    background: var(--panel-white);
  }
  .panel--lid { top: 0; height: 243px; border-bottom: 1px solid var(--fold-line); }
  .panel--front { top: 243px; height: 459px; border-bottom: 1px solid var(--fold-line); }
  .panel--base { top: 702px; height: 243px; }

  .art-area { position: absolute; }
  .panel--lid .art-area {
    left: 790px; top: 0; width: 308px; height: 243px;
    background: linear-gradient(90deg, var(--tone-warm-light), var(--tone-warm));
  }
  .panel--front .art-area {
    left: 180px; top: 0; width: 840px; height: 459px;
    background: linear-gradient(90deg, var(--tone-cool-light), var(--tone-pink) 50%, var(--tone-warm-light));
  }
  .panel--base .art-area {
    left: 0; top: 0; width: 270px; height: 243px;
    background: linear-gradient(90deg, var(--tone-pink), var(--tone-cool-light));
  }

  .name-badge {
    position: absolute;
    left: 50%;
    text-align: center;
    font-family: "Montserrat", sans-serif;
    font-weight: 800;
    color: var(--ink);
    line-height: 1.1;
    letter-spacing: 0.02em;
    text-transform: uppercase;
    white-space: nowrap;
  }
  .name-badge__dot {
    display: block;
    margin: 0 auto 10px;
    border-radius: 50%;
    background: var(--accent-blue);
  }
  .panel--lid .name-badge {
    top: 48px;
    font-size: 30px;
    transform: translateX(-50%) rotate(180deg);
  }
  .panel--base .name-badge {
    top: 48px;
    font-size: 30px;
    transform: translateX(-50%);
  }
  .panel--lid .name-badge__dot,
  .panel--base .name-badge__dot { width: 40px; height: 40px; }

  .seal {
    position: absolute;
    left: 414px;
    top: 94px;
    width: 272px;
    height: 272px;
    border-radius: 50%;
    background: var(--panel-white);
  }
  .seal .name-badge {
    top: 58px;
    font-size: 32px;
    transform: translateX(-50%);
  }
  .seal .name-badge__dot { width: 48px; height: 48px; }
</style>
</head>
<body>
  <main class="wrap-sheet">
    <div class="dieline">
      <section class="panel panel--lid">
        <div class="art-area" role="img" aria-label="Colour powder splash in red, orange, yellow and green"></div>
        <div class="name-badge"><span class="name-badge__dot"></span>Cedar<br>Vitality</div>
      </section>
      <section class="panel panel--front">
        <div class="art-area" role="img" aria-label="Large rainbow colour powder explosion behind the seal"></div>
        <div class="seal">
          <div class="name-badge"><span class="name-badge__dot"></span>Cedar<br>Vitality</div>
        </div>
      </section>
      <section class="panel panel--base">
        <div class="art-area" role="img" aria-label="Colour powder splash in pink, purple and blue"></div>
        <div class="name-badge"><span class="name-badge__dot"></span>Cedar<br>Vitality</div>
      </section>
    </div>
  </main>
</body>
</html>
```